CordaMax Packaging, for retail brand of graduation tassels

Retail packaging for graduation tassels. Leave space for a UPC on the back bottom of the template. Design must bleed over edges for printing. Use the attached logo in the packaging. The photo is an example of the packaging, but does not match the template. Please use the shape and dimensions of the template. Please provide all standard file formats. The packaging is not specific to a SKU, it is general.
You can change the color of the logo and add the "TM"

Font styles to use
Other font styles liked:
• See logo

Colors

Designer to choose colors to be used in the design.

Requirements
Must have
• Brand logo, color bleeds on the template
• Include any or all of the following information, either on the back or used as call outs on the packaging.
• "Our tassels are made from the highest quality of polyester available, resulting in accurate and consistent school colors. Each tassel has 50-60 braided yarns. The signets are made from Zinc alloy or solid brass (depending on color)"
Nice to have
• gets the attention of consumers
Should not have
• nothing specific to a SKU

```html
<!DOCTYPE html>
<html lang="en">
<head>
<meta charset="utf-8">
<title>CordaMax Graduation Tassel Box — Dieline</title>
<link rel="stylesheet" href="https://fonts.googleapis.com/css2?family=PT+Sans+Narrow:wght@400;700&family=Great+Vibes&display=swap">
<style>
  :root {
    --stage: #e3e5e7;
    --board: #141414;
    --board-edge: #3a3a3a;
    --silver: #d9d9d9;
    --logo-silver: #c4c6c8;
    --window: #ffffff;
    --sku-text: #8a8a8a;
  }
  html, body {
    margin: 0;
    padding: 0;
    width: 1200px;
    height: 923px;
    overflow: hidden;
    background: var(--stage);
  }
  .canvas {
    position: relative;
    width: 1200px;
    height: 923px;
    display: flex;
    align-items: center;
    justify-content: center;
  }
  .dieline { display: block; }
  .panel { fill: var(--board); stroke: var(--board-edge); stroke-width: 0.8; }
  .window { fill: var(--window); }
  .hang-hole { fill: var(--window); }
  .brand {
    font-family: "PT Sans Narrow", sans-serif;
    font-weight: 700;
    fill: var(--logo-silver);
    letter-spacing: 0.5px;
  }
  .copy {
    font-family: "PT Sans Narrow", sans-serif;
    font-weight: 400;
    font-size: 12.5px;
    fill: var(--silver);
    text-anchor: middle;
  }
  .tagline {
    font-family: "PT Sans Narrow", sans-serif;
    font-size: 12px;
    fill: var(--silver);
  }
  .premium {
    font-family: "Great Vibes", cursive;
    font-size: 16px;
    fill: var(--silver);
  }
  .icon { fill: none; stroke: var(--silver); stroke-width: 1.6; }
  .sku-box { fill: var(--window); }
  .sku-label {
    font-family: "PT Sans Narrow", sans-serif;
    font-size: 24px;
    fill: var(--sku-text);
    text-anchor: middle;
  }
</style>
</head>
<body>
<main class="canvas">
  <svg class="dieline" width="441" height="900" viewBox="700 20 480 980" xmlns="http://www.w3.org/2000/svg" aria-label="CordaMax graduation tassel box, flat dieline">

    <!-- glue flap -->
    <polygon class="panel glue-flap" points="762,175 803,155 803,960 762,940"/>

    <!-- back panel with hang tab -->
    <path class="panel back-hang-tab" d="M803,155 V48 L813,38 H905 L915,48 V155 Z"/>
    <circle class="hang-hole" cx="859" cy="75" r="11"/>
    <circle class="hang-hole" cx="859" cy="117" r="11"/>
    <rect class="panel back-panel" x="803" y="155" width="112" height="805"/>
    <polygon class="panel back-bottom-flap" points="803,960 915,960 905,990 813,990"/>

    <!-- left side panel -->
    <path class="panel side-top-flap" d="M918,155 V120 L926,108 H958 L965,120 V155 Z"/>
    <rect class="panel side-panel" x="918" y="155" width="47" height="805"/>
    <polygon class="panel side-bottom-flap" points="918,960 965,960 958,982 925,982"/>

    <!-- front panel with tuck -->
    <path class="panel front-tuck" d="M965,155 V80 Q965,68 977,68 H1068 Q1080,68 1080,80 V155 Z"/>
    <rect class="panel front-panel" x="965" y="155" width="115" height="805"/>
    <path class="panel front-bottom-flap" d="M965,960 H1080 V990 H1058 V975 H987 V990 H965 Z"/>

    <!-- right side panel -->
    <path class="panel side-top-flap" d="M1082,155 V120 L1088,108 H1114 L1120,120 V155 Z"/>
    <rect class="panel side-panel" x="1082" y="155" width="38" height="805"/>
    <polygon class="panel side-bottom-flap" points="1082,960 1120,960 1114,982 1088,982"/>

    <!-- back panel copy -->
    <g class="back-copy">
      <ellipse class="icon" cx="859" cy="240" rx="17" ry="4"/>
      <ellipse class="icon" cx="859" cy="244" rx="17" ry="4"/>
      <text class="copy" x="859" y="264">Our tassels</text>
      <text class="copy" x="859" y="281">are made</text>
      <text class="copy" x="859" y="297">from the</text>
      <text class="copy" x="859" y="314">highest quality</text>
      <text class="copy" x="859" y="330">of polyester</text>
      <text class="copy" x="859" y="347">available,</text>
      <text class="copy" x="859" y="363">resulting</text>
      <text class="copy" x="859" y="380">in accurate</text>
      <text class="copy" x="859" y="396">and</text>
      <text class="copy" x="859" y="413">consistent</text>
      <text class="copy" x="859" y="429">school colors.</text>

      <path class="icon" d="M843,459 l6,5 l-6,5 M851,459 l6,5 l-6,5 M859,459 l6,5 l-6,5 M867,459 l6,5 l-6,5 M843,464 H877"/>
      <text class="copy" x="859" y="495">Each tassel has</text>
      <text class="copy" x="859" y="512">50-60</text>
      <text class="copy" x="859" y="528">braided yarns.</text>

      <ellipse class="icon" cx="859" cy="561" rx="18" ry="4"/>
      <ellipse class="icon" cx="859" cy="567" rx="18" ry="4"/>
      <ellipse class="icon" cx="859" cy="573" rx="18" ry="4"/>
      <text class="copy" x="859" y="595">The signets</text>
      <text class="copy" x="859" y="611">are made from</text>
      <text class="copy" x="859" y="628">Zinc Alloy</text>
      <text class="copy" x="859" y="644">or Solid Brass.</text>

      <rect class="sku-box" x="803" y="912" width="112" height="32"/>
      <text class="sku-label" x="859" y="938">SKU</text>
    </g>

    <!-- left side panel text -->
    <text class="brand" font-size="26" transform="translate(931,168) rotate(90)">CordaMax</text>
    <text class="premium" transform="translate(946,785) rotate(90)">~ Premium ~</text>
    <text class="tagline" transform="translate(933,858) rotate(90)">Graduation Tassel</text>

    <!-- front panel -->
    <text class="brand" font-size="22" x="1022" y="142" text-anchor="middle">CordaMax</text>
    <path class="window" role="img" aria-label="Display window showing the tassel inside"
          d="M1003,220 A20,20 0 0 1 1043,220 V295 H1051 A10,10 0 0 1 1061,305 V335 A10,10 0 0 1 1051,345 H1043 V728 H1003 V345 H995 A10,10 0 0 1 985,335 V305 A10,10 0 0 1 995,295 H1003 Z"/>
    <text class="brand" font-size="28" x="1022" y="808" text-anchor="middle">CordaMax</text>
    <text class="premium" x="1022" y="900" text-anchor="middle">~ Premium ~</text>
    <text class="tagline" x="1022" y="918" text-anchor="middle">Graduation</text>
    <text class="tagline" x="1022" y="931" text-anchor="middle">Tassel</text>

    <!-- right side panel text -->
    <text class="brand" font-size="26" transform="translate(1092,168) rotate(90)">CordaMax</text>
    <text class="tagline" transform="translate(1110,852) rotate(-90)">Graduation Tassel</text>
    <text class="premium" transform="translate(1112,932) rotate(-90)">~ Premium ~</text>
  </svg>
</main>
</body>
</html>
```